Website for Swedish wellness company "Heartmeadow"

We need a website for our Swedish wellness company. The name is "Heartmeadow" . The company is all about sustainablility for our body, soul and planet. We work with coaching, yoga, massage, healthy food, retreats(sports, excercise, sufing), healing and inspirational talks. We are convinced that personal sustainability and a strong spiritual connection to yourself will lead to planetary sustainability. Our customers are both companies and consumers from all over the world. The final design should be clean/simple and you should get a feeling of community, happiness, warmth, connection,, joy, spirituality but still a professional touch.Just got a logo from Pixel Harbor and are very happy with it;-)
Updates

Sorry I was too enthusiastic posting this project. Of course I will give you some text as well för the different pages! I will see to that it is finished by friday so if you want to wait with your submissions please do! Best regards Maria

Target Market(s)

Businesses and consumers

Industry/Entity Type

Health And Wellness

Number of Pages Required

5+ page

Font styles to use
Sans Serif

Colors
33a6d7
00a990
b7a5cd

Requirements
Must have
• Idea about pages:
• I am not sure how many pages I get for the price, but 5 would be nice to start with.
• Not sure what write ups is;-)
• But title of the pages could be:
• Landing page
• About us
• Services
• Retreats
• Contact us
Nice to have
• A clean and professional website but with some heart and soul in it. Because we Would love colours that harmonize with our logo, but other ideas are welcome!

```html
<!DOCTYPE html>
<html lang="en">
<head>
<meta charset="utf-8">
<title>Heartmeadow — Swedish wellness studio</title>
<link rel="stylesheet" href="https://fonts.googleapis.com/css2?family=Mulish:wght@400;600;700;800&display=swap">
<style>
:root{
  --teal:#1ba5b5;
  --navy:#1b3a6b;
  --navy-deep:#0c2c66;
  --text:#6d6d6d;
  --light:#f2f2f2;
  --white:#ffffff;
}
*{box-sizing:border-box;margin:0;padding:0}
html,body{width:1200px;height:3436px;overflow:hidden}
body{font-family:"Mulish",sans-serif;color:var(--text);background:var(--white);position:relative}
a{text-decoration:none;color:inherit}

/* header */
.site-header{height:150px;position:relative;background:var(--white)}
.brand{position:absolute;left:70px;top:16px;display:flex;flex-direction:column;align-items:center}
.brand-dot{width:52px;height:52px;border-radius:50%;background:var(--teal)}
.brand-name{margin-top:6px;font-weight:800;font-size:22px;letter-spacing:1px;color:var(--navy);text-transform:uppercase}
.call{position:absolute;right:86px;top:24px;display:flex;align-items:center;gap:14px;color:var(--teal);font-weight:700;font-size:17px}
.call-icon{width:46px;height:46px;border:2px solid var(--teal);border-radius:50%;display:flex;align-items:center;justify-content:center}
.main-nav{position:absolute;right:60px;top:100px;display:flex}
.main-nav a{font-size:13px;font-weight:700;color:var(--navy);padding:6px 20px;text-transform:uppercase}
.main-nav a.active{color:var(--teal);border-bottom:2px solid var(--teal)}

/* hero */
.hero{position:relative;height:710px}
.hero-photo{position:absolute;inset:0;background:linear-gradient(180deg,#9fc6d8 0%,#c9d9df 35%,#6c8a94 62%,#4a4a44 100%)}
.hero-copy{position:absolute;left:120px;top:110px;color:var(--white);padding:14px 20px;background:rgba(255,255,255,.14)}
.hero-copy h1{font-size:58px;font-weight:800;letter-spacing:1px;line-height:1.1}
.hero-copy p{margin-top:10px;font-size:19px;font-weight:700;line-height:1.45;max-width:430px}
.hero-wave{position:absolute;left:0;bottom:0;width:1200px;height:120px}

/* welcome */
.welcome{position:relative;height:492px}
.welcome-copy{position:absolute;left:112px;top:56px;width:640px}
.welcome-copy h2{font-size:38px;font-weight:700;color:var(--navy)}
.welcome-copy h2 span{color:var(--teal)}
.welcome-copy p{margin-top:22px;font-size:14px;line-height:1.75}
.btn{display:inline-block;background:var(--teal);color:var(--white);font-weight:700;font-size:16px;padding:16px 34px;border-radius:30px}
.welcome-copy .btn{margin-top:32px}
.welcome-mark{position:absolute;left:790px;top:60px;width:290px;height:290px;border-radius:50%;border:16px solid var(--teal);display:flex;align-items:center;justify-content:center;color:var(--navy);font-weight:800;font-size:28px}

/* services */
.services{background:var(--light);height:708px;position:relative;text-align:center}
.section-title{font-size:38px;font-weight:700;color:var(--navy);padding-top:60px}
.section-title span{color:var(--teal)}
.service-grid{position:absolute;left:130px;top:150px;width:940px;display:grid;grid-template-columns:repeat(3,1fr);row-gap:48px}
.service-icon{width:132px;height:132px;margin:0 auto;border-radius:50%;background:var(--teal);display:flex;align-items:center;justify-content:center;box-shadow:0 0 0 8px rgba(27,165,181,.18)}
.service h3{margin-top:20px;font-size:20px;font-weight:700;color:var(--navy)}
.service p{margin:12px auto 0;width:220px;font-size:12px;line-height:1.7}

/* banner */
.banner{position:relative;height:448px;color:var(--white);text-align:center}
.banner-photo{position:absolute;inset:0;background:linear-gradient(90deg,#1a8fb0 0%,#2aa9b0 55%,#3eb3a8 100%)}
.banner-copy{position:relative;padding-top:250px}
.banner-copy h2{font-size:34px;font-weight:800;letter-spacing:1px}
.banner-copy p{margin-top:14px;font-size:16px;font-weight:600;letter-spacing:1px}
.btn-outline{display:inline-block;margin-top:28px;border:2px solid var(--white);border-radius:30px;padding:16px 40px;font-size:14px;font-weight:700}

/* news */
.news{height:600px;position:relative;text-align:center}
.news .section-title{padding-top:50px}
.news-grid{position:absolute;left:110px;top:160px;width:980px;display:grid;grid-template-columns:repeat(3,1fr);column-gap:40px;text-align:left}
.news-photo{height:240px;position:relative}
.date{position:absolute;left:0;top:95px;width:44px;height:72px;background:var(--teal);color:var(--white);text-align:center;font-weight:800;font-size:18px;padding-top:22px;line-height:1}
.date small{display:block;font-size:11px;font-weight:600;margin-top:4px}
.news-card h3{margin-top:26px;font-size:19px;font-weight:700;color:var(--navy)}
.news-card p{margin-top:12px;font-size:12px;line-height:1.7}
.news-card a{display:block;margin-top:16px;font-size:13px;font-weight:700;color:var(--teal);text-transform:uppercase}

/* footer */
.site-footer{position:absolute;left:0;top:3108px;width:1200px;height:328px;background:var(--navy-deep);color:var(--white);text-align:center}
.footer-brand{padding-top:50px;display:flex;flex-direction:column;align-items:center}
.footer-brand .brand-dot{background:var(--white)}
.footer-brand .brand-name{color:var(--white);font-size:26px}
.footer-nav{margin-top:44px;display:flex;justify-content:center;font-size:13px;font-weight:700}
.footer-nav a{padding:0 30px;border-right:1px solid rgba(255,255,255,.6)}
.footer-nav a:last-child{border-right:0}
.copyright{margin-top:44px;font-size:12px;opacity:.85}
</style>
</head>
<body>

<header class="site-header">
  <div class="brand"><span class="brand-dot"></span><span class="brand-name">Heartmeadow</span></div>
  <div class="call">
    <span class="call-icon">
      <svg width="22" height="22" viewBox="0 0 24 24"><path fill="#1ba5b5" d="M6.6 10.8c1.4 2.8 3.8 5.1 6.6 6.6l2.2-2.2c.3-.3.7-.4 1-.2 1.1.4 2.3.6 3.6.6.6 0 1 .4 1 1V20c0 .6-.4 1-1 1C10.6 21 3 13.4 3 4c0-.6.4-1 1-1h3.5c.6 0 1 .4 1 1 0 1.3.2 2.5.6 3.6.1.3 0 .7-.2 1z"/></svg>
    </span>
    CALL US : 000-456-7890
  </div>
  <nav class="main-nav">
    <a href="#" class="active">Home</a><a href="#">About us</a><a href="#">Services</a><a href="#">Retreats</a><a href="#">Contact us</a>
  </nav>
</header>

<section class="hero">
  <div class="hero-photo" role="img" aria-label="Woman meditating in a yoga pose on seaside rocks under a cloudy sky"></div>
  <div class="hero-copy">
    <h1>Heartmeadow</h1>
    <p>Sed ut perspiciatis unde omnis iste natus error sit voluptatem accusantium</p>
  </div>
  <svg class="hero-wave" viewBox="0 0 1200 120" preserveAspectRatio="none">
    <path d="M0 70 C300 10 600 130 900 60 C1020 32 1120 40 1200 60 L1200 120 L0 120Z" fill="#ffffff"/>
    <path d="M0 80 C300 20 600 140 900 70 C1020 42 1120 50 1200 70" fill="none" stroke="#1ba5b5" stroke-width="6"/>
  </svg>
</section>

<section class="welcome">
  <div class="welcome-copy">
    <h2>Welcome to <span>Heartmeadow</span></h2>
    <p>Sed ut perspiciatis unde omnis iste natus error sit voluptatem accusantium doloremque laudantium, totam rem aperiam, eaque ipsa quae ab illo inventore veritatis et quasi architecto beatae vitae dicta sunt explicabo. Nemo enim ipsam voluptatem quia voluptas sit aspernatur aut odit aut fugit, sed quia consequuntur magni dolores eos qui ratione voluptatem sequi nesciunt.</p>
    <p>Neque porro quisquam est, qui dolorem ipsum quia dolor sit amet, consectetur, adipisci velit, sed quia non numquam eius modi tempora incidunt ut labore et dolore magnam aliquam quaerat voluptatem.</p>
    <a href="#" class="btn">Read More</a>
  </div>
  <div class="welcome-mark">Heartmeadow</div>
</section>

<section class="services">
  <h2 class="section-title">Our <span>Services</span></h2>
  <div class="service-grid">
    <div class="service"><div class="service-icon"><svg width="56" height="56" viewBox="0 0 56 56"><circle cx="28" cy="28" r="20" fill="none" stroke="#fff" stroke-width="4"/></svg></div><h3>Yoga</h3><p>Sed ut perspiciatis unde omnis iste natus error sit voluptatem accusantium</p></div>
    <div class="service"><div class="service-icon"><svg width="56" height="56" viewBox="0 0 56 56"><rect x="8" y="26" width="40" height="8" rx="3" fill="#fff"/><rect x="12" y="34" width="4" height="10" fill="#fff"/><rect x="40" y="34" width="4" height="10" fill="#fff"/></svg></div><h3>Massage</h3><p>Sed ut perspiciatis unde omnis iste natus error sit voluptatem accusantium</p></div>
    <div class="service"><div class="service-icon"><svg width="56" height="56" viewBox="0 0 56 56"><circle cx="28" cy="32" r="16" fill="#fff"/><path d="M28 16 C30 8 38 8 40 10 C36 14 32 16 28 16Z" fill="#fff"/></svg></div><h3>Healthy Food</h3><p>Sed ut perspiciatis unde omnis iste natus error sit voluptatem accusantium</p></div>
    <div class="service"><div class="service-icon"><svg width="56" height="56" viewBox="0 0 56 56"><path d="M6 46 L22 20 L32 34 L38 26 L50 46Z" fill="#fff"/></svg></div><h3>Retreats</h3><p>Sed ut perspiciatis unde omnis iste natus error sit voluptatem accusantium</p></div>
    <div class="service"><div class="service-icon"><svg width="56" height="56" viewBox="0 0 56 56"><path d="M28 46 C14 36 8 28 8 20 C8 13 13 9 18 9 C22 9 26 12 28 15 C30 12 34 9 38 9 C43 9 48 13 48 20 C48 28 42 36 28 46Z" fill="#fff"/></svg></div><h3>Healing</h3><p>Sed ut perspiciatis unde omnis iste natus error sit voluptatem accusantium</p></div>
    <div class="service"><div class="service-icon"><svg width="56" height="56" viewBox="0 0 56 56"><rect x="6" y="10" width="32" height="22" rx="4" fill="#fff"/><path d="M12 32 L12 40 L20 32Z" fill="#fff"/><rect x="22" y="22" width="28" height="18" rx="4" fill="none" stroke="#fff" stroke-width="3"/></svg></div><h3>Inspirational Talks</h3><p>Sed ut perspiciatis unde omnis iste natus error sit voluptatem accusantium</p></div>
  </div>
</section>

<section class="banner">
  <div class="banner-photo" role="img" aria-label="Group yoga class stretching in a bright studio under a teal overlay"></div>
  <div class="banner-copy">
    <h2>SED UT PERSPICIATIS UNDE OMNIS ISTE NATUS</h2>
    <p>VOLUPTATEM ACCUSANTIUM DOLOREMQUE LAUDANTIUM</p>
    <a href="#" class="btn-outline">CLICK HERE FOR MORE INFO</a>
  </div>
</section>

<section class="news">
  <h2 class="section-title">Latest <span>News</span></h2>
  <div class="news-grid">
    <article class="news-card">
      <div class="news-photo" role="img" aria-label="Relaxing spa massage with towels and candles" style="background:linear-gradient(135deg,#c8b9a8,#8f7a66)"><span class="date">02<small>JAN</small></span></div>
      <h3>Sed ut perspiciatis unde omnis</h3>
      <p>Sed ut perspiciatis unde omnis iste natus error sit voluptatem accusantium doloremque laudantium, totam rem aperiam, eaque ipsa quae ab illo.</p>
      <a href="#">Read more</a>
    </article>
    <article class="news-card">
      <div class="news-photo" role="img" aria-label="Fresh green salad bowl with vegetables" style="background:linear-gradient(135deg,#7c9a3c,#b2452f)"><span class="date">02<small>JAN</small></span></div>
      <h3>Sed ut perspiciatis unde omnis</h3>
      <p>Sed ut perspiciatis unde omnis iste natus error sit voluptatem accusantium doloremque laudantium, totam rem aperiam, eaque ipsa quae ab illo.</p>
      <a href="#">Read more</a>
    </article>
    <article class="news-card">
      <div class="news-photo" role="img" aria-label="Yoga class practising poses in a sunlit studio" style="background:linear-gradient(135deg,#e6e2dc,#8c857d)"><span class="date">02<small>JAN</small></span></div>
      <h3>Sed ut perspiciatis unde omnis</h3>
      <p>Sed ut perspiciatis unde omnis iste natus error sit voluptatem accusantium doloremque laudantium, totam rem aperiam, eaque ipsa quae ab illo.</p>
      <a href="#">Read more</a>
    </article>
  </div>
</section>

<footer class="site-footer">
  <div class="footer-brand"><span class="brand-dot"></span><span class="brand-name">Heartmeadow</span></div>
  <nav class="footer-nav"><a href="#">HOME</a><a href="#">ABOUT US</a><a href="#">SERVICES</a><a href="#">RETREATS</a><a href="#">CONTACT US</a></nav>
  <p class="copyright">© Copyright 2019 Heartmeadow. All rights reserved.</p>
</footer>

</body>
</html>
```